LEARN Business Skills so you can Earn a good living

size of the poster is 8”x 10.75" plus 0.25" bleed.
Please leave 1 inch on the bottoum for footer
I want a design a poster that will attract people's attention.
I appreciate a creative ad however the ad should not take away from being able to clearly read the text.
-I also appreciate a simple creative ad that is not too busy.
-you can use graphics, vectors, or pictures of real people.
-however, if you use real people it should be a white male that is wearing a white shirt and look like a professional person.

Target Market(s)

Potential young business people

Industry/Entity Type

education

Requirements
Must have
• easy to read the text
Nice to have
• I would like a "creative" simple ad that is easy to be read
Should not have
• pictures of women

```html
<!DOCTYPE html>
<html lang="en">
<head>
<meta charset="utf-8">
<title>Learn to Earn – Business Enrichment Course</title>
<link rel="stylesheet" href="https://fonts.googleapis.com/css2?family=Montserrat:ital,wght@0,600;0,700;0,800;0,900;1,500;1,600&family=Open+Sans:wght@400;600&display=swap">
<style>
  :root {
    --backdrop: #e6e6e6;
    --paper: #ffffff;
    --brand-blue: #2f6fc1;
    --navy: #1d2f57;
    --orange: #ee5a24;
    --wave-grey: #9aa3ad;
    --footer-band: #f0f1f2;
    --footer-text: #9a9fa6;
    --photo-light: #f7f5f2;
    --photo-mid: #e9e2da;
    --photo-shirt: #fbfbfd;
  }
  * { margin: 0; padding: 0; box-sizing: border-box; }
  html, body {
    width: 1200px;
    height: 2820px;
    overflow: hidden;
    background: var(--backdrop);
  }
  .flyer {
    position: absolute;
    left: 40px;
    top: 669px;
    width: 1120px;
    height: 1482px;
    background: var(--paper);
    overflow: hidden;
    box-shadow: 0 6px 24px rgba(0,0,0,.12);
  }
  .hero-photo {
    position: absolute;
    left: 500px;
    top: 0;
    width: 620px;
    height: 1060px;
    background:
      radial-gradient(ellipse 45% 28% at 55% 30%, var(--photo-mid) 0%, rgba(233,226,218,0) 100%),
      radial-gradient(ellipse 70% 45% at 55% 85%, var(--photo-shirt) 0%, rgba(251,251,253,0) 100%),
      linear-gradient(90deg, var(--paper) 0%, var(--photo-light) 35%, var(--photo-light) 100%);
  }
  .headline {
    position: absolute;
    left: 52px;
    top: 54px;
    font-family: "Montserrat", sans-serif;
    font-weight: 900;
    color: var(--brand-blue);
    line-height: .92;
  }
  .headline__word { display: block; font-size: 138px; letter-spacing: -2px; }
  .headline__joiner {
    display: block;
    font-size: 58px;
    font-weight: 800;
    color: var(--orange);
    margin: 0 0 4px 6px;
  }
  .course-badge {
    position: absolute;
    left: 52px;
    top: 370px;
    width: 560px;
    background: var(--orange);
    outline: 3px solid var(--orange);
    outline-offset: 8px;
    border: 3px solid var(--paper);
    padding: 18px 26px 20px;
    font-family: "Montserrat", sans-serif;
    font-weight: 800;
    font-size: 56px;
    line-height: 1.0;
    color: var(--paper);
    letter-spacing: -.5px;
  }
  .tagline {
    position: absolute;
    left: 52px;
    top: 612px;
    font-family: "Montserrat", sans-serif;
    font-style: italic;
    font-weight: 600;
    font-size: 35px;
    line-height: 1.18;
    color: var(--brand-blue);
  }
  .skills-intro {
    position: absolute;
    left: 52px;
    top: 724px;
    font-family: "Montserrat", sans-serif;
    font-weight: 800;
    font-size: 31px;
    line-height: 1.2;
    color: var(--navy);
  }
  .benefits {
    position: absolute;
    left: 52px;
    top: 822px;
    list-style: none;
    font-family: "Montserrat", sans-serif;
    font-weight: 800;
    font-size: 36px;
    line-height: 1.42;
  }
  .benefits .accent-orange { color: var(--orange); }
  .benefits .accent-blue { color: var(--brand-blue); }
  .wave {
    position: absolute;
    left: 0;
    top: 900px;
    width: 1120px;
    height: 260px;
  }
  .topics {
    position: absolute;
    left: 52px;
    top: 1148px;
    width: 1016px;
    display: grid;
    grid-template-columns: 320px 430px 1fr;
    font-family: "Open Sans", sans-serif;
    font-size: 19px;
    line-height: 1.4;
    color: var(--brand-blue);
  }
  .topics ul { list-style: none; }
  .topics li { position: relative; padding-left: 18px; white-space: nowrap; }
  .topics li::before {
    content: "";
    position: absolute;
    left: 2px;
    top: 11px;
    width: 6px;
    height: 6px;
    border-radius: 50%;
    background: var(--brand-blue);
  }
  .footer-space {
    position: absolute;
    left: 0;
    bottom: 0;
    width: 100%;
    height: 112px;
    background: var(--footer-band);
    display: flex;
    align-items: center;
    justify-content: center;
    font-family: "Montserrat", sans-serif;
    font-weight: 700;
    font-size: 30px;
    letter-spacing: 1px;
    color: var(--footer-text);
  }
</style>
</head>
<body>
  <main class="flyer">
    <div class="hero-photo" role="img" aria-label="Photo of a smiling professional man with glasses and a beard, wearing a white shirt, resting his chin on his hand"></div>

    <h1 class="headline">
      <span class="headline__word">LEARN</span>
      <span class="headline__joiner">to</span>
      <span class="headline__word">EARN</span>
    </h1>

    <div class="course-badge">BUSINESS<br>ENRICHMENT<br>COURSE</div>

    <p class="tagline">A proven success of helping<br>people in their livelihoods</p>

    <p class="skills-intro">BUSINESS SKILLS THAT<br>WILL HELP YOU:</p>

    <ul class="benefits">
      <li><span class="accent-orange">GET A QUALITY JOB</span></li>
      <li><span class="accent-blue">START/GROW YOUR BUSINESS</span></li>
      <li><span class="accent-orange">INCREASE YOUR</span> <span class="accent-blue">SALARY</span></li>
    </ul>

    <svg class="wave" viewBox="0 0 1120 260" preserveAspectRatio="none" aria-hidden="true">
      <path d="M0 210 C380 262 760 200 1120 96 L1120 260 L0 260 Z" fill="var(--paper)"/>
      <path d="M0 138 C360 222 760 118 1120 6" fill="none" stroke="var(--orange)" stroke-width="5"/>
      <path d="M0 160 C360 240 760 138 1120 30 L1120 100 C760 204 380 262 0 212 Z" fill="var(--brand-blue)"/>
      <path d="M0 226 C380 276 760 214 1120 112" fill="none" stroke="var(--wave-grey)" stroke-width="4"/>
    </svg>

    <section class="topics" aria-label="Course topics">
      <ul>
        <li>Business Administration</li>
        <li>Investments</li>
        <li>Sales/ Marketing</li>
        <li>Public Speaking</li>
        <li>Distribution</li>
        <li>Real Estate</li>
        <li>Online Selling</li>
      </ul>
      <ul>
        <li>Small Business Management</li>
        <li>Computers</li>
        <li>Business Law</li>
        <li>Import/Export</li>
        <li>Marketing</li>
        <li>Health Care</li>
        <li>Project Management Interviewing Skills</li>
      </ul>
      <ul>
        <li>Finance</li>
        <li>Accounting</li>
        <li>Negotiation</li>
        <li>Information Technology</li>
        <li>Bookkeeping Software</li>
        <li>Management</li>
      </ul>
    </section>

    <footer class="footer-space">BOTTOUM FOR FOOTER</footer>
  </main>
</body>
</html>
```